Lien Post Card - (5.5 x 8.5)

FRONT OF POSTCARD
Is a Property Lien Putting Your Home at Risk?
HOA Liens • Tax Liens • Municipal Charges • Other Property-Related Liens
You may have options to resolve outstanding liens and protect your home.
A Refinance or Home Equity Line of Credit (HELOC) may help you:
✔ Pay off qualifying liens
✔ Consolidate debt into one manageable payment
✔ Access your home's equity
✔ Improve your financial flexibility
✔ Avoid additional penalties, fees, or collection actions
Don't wait until the situation becomes more difficult.
Call today for a confidential review of your options.
Bluegate Lending Partners, Inc.
(800) 647-2915 x 42
www.bluegatelendco.com
NMLS #381640
BACK OF POSTCARD
Your Home Equity Could Be the Solution
If you have received notices regarding:
• Delinquent Property Taxes
• HOA or Condo Association Assessments
• Municipal Utility Liens
• Special Assessments
• Other Property-Related Obligations
You may qualify for financing options designed to help satisfy those obligations and bring your property current.
Our experienced mortgage professionals can review your situation and discuss available programs, including:
• Cash-Out Refinancing
• Home Equity Lines of Credit (HELOCs)
• Home Equity Loans
• Debt Consolidation Solutions
Free Consultation • No Obligation
Contact Marcus Delaney today at (800) 647-2915 x42 or mdelaney@bluegatelendco.com (NMLS #57308)

```html
<!DOCTYPE html>
<html lang="en">
<head>
<meta charset="utf-8">
<title>Bluegate Lending Partners – Lien Postcard</title>
<link href="https://fonts.googleapis.com/css2?family=Oswald:wght@500;600;700&family=Roboto:ital,wght@0,400;0,500;0,700;1,400;1,700&family=Roboto+Condensed:wght@500;700&family=Great+Vibes&display=swap" rel="stylesheet">
<style>
:root{
  --navy:#0d2466;
  --navy-deep:#081a4d;
  --royal:#1d47a8;
  --ink:#1a1f2e;
  --gold:#f2c230;
  --gold-deep:#c9901c;
  --gold-light:#ffe08a;
  --paper:#ffffff;
  --mist:#eef2f8;
  --stage:#d9d9d9;
}
*{margin:0;padding:0;box-sizing:border-box}
html,body{width:1200px;height:1200px;overflow:hidden}
body{background:var(--stage);font-family:"Roboto",sans-serif;color:var(--ink);position:relative}
.brand-band{position:absolute;left:0;top:0;width:1200px;height:362px;background:var(--paper);display:flex;align-items:center;justify-content:center;gap:18px}
.brand-band .dot{width:34px;height:34px;border-radius:50%;background:var(--royal)}
.brand-band .name{font-family:"Oswald",sans-serif;font-weight:700;font-size:52px;color:var(--royal);letter-spacing:1px}
.card{position:absolute;top:457px;width:530px;height:646px;overflow:hidden}
.card-front{left:71px;background:linear-gradient(180deg,#1a3f96 0%,var(--navy) 60%,var(--navy-deep) 100%)}
.card-back{left:617px;background:var(--paper)}
.abs{position:absolute}
.ph{position:absolute}
/* front */
.photo-collage{left:0;top:0;width:530px;height:175px;background:linear-gradient(180deg,#6b7fa3 0%,#c9a255 45%,#3a4c78 100%)}
.photo-advisor{left:345px;top:135px;width:185px;height:235px;background:linear-gradient(160deg,#2a3d7a 0%,#1b1f2e 60%,#3a2c24 100%)}
.head-fade{left:0;top:110px;width:530px;height:80px;background:linear-gradient(180deg,rgba(26,63,150,0) 0%,#1a3f96 100%)}
.headline{left:20px;top:0;width:340px;height:280px;color:#fff;font-family:"Roboto",sans-serif;font-weight:700;z-index:2}
.headline span{position:absolute;left:0;white-space:nowrap}
.headline .small{top:126px;left:42px;font-size:28px;line-height:30px}
.headline .big{top:153px;font-family:"Oswald",sans-serif;font-size:54px;line-height:54px;color:var(--gold);letter-spacing:.3px}
.headline .mid{font-size:35px;line-height:36px}
.headline .l3{top:205px}
.headline .l4{top:241px}
.headline .gold{position:static;color:var(--gold)}
.lien-band{left:-10px;top:280px;width:355px;height:42px;background:linear-gradient(90deg,var(--navy-deep),var(--royal));transform:skewX(-12deg);border-right:3px solid var(--gold)}
.lien-text{left:26px;top:283px;width:320px;color:#fff;font-family:"Roboto Condensed",sans-serif;font-weight:700;font-size:14.5px;line-height:18px}
.lien-text b{color:var(--gold);padding:0 4px}
.options{left:0;top:323px;width:345px;height:44px;background:linear-gradient(90deg,#fff 60%,rgba(255,255,255,.85));}
.options p{position:absolute;left:20px;top:5px;font-size:13px;line-height:17px;color:#223}
.options em{color:var(--navy);font-weight:700}
.benefits-bg{left:0;top:367px;width:530px;height:110px;background:linear-gradient(90deg,#fff 45%,var(--mist) 100%)}
.photo-house-front{left:290px;top:350px;width:240px;height:127px;background:linear-gradient(90deg,rgba(255,255,255,1) 0%,rgba(255,255,255,0) 35%),linear-gradient(180deg,#b8c9dc 0%,#9c8a72 55%,#4f7a3a 100%)}
.benefits{left:0;top:367px;width:530px;height:110px;z-index:2}
.benefits h3{position:absolute;left:20px;top:6px;font-family:"Roboto Condensed",sans-serif;font-size:11.5px;color:var(--navy);font-weight:700;white-space:nowrap}
.benefits ul{position:absolute;left:20px;top:23px;list-style:none}
.benefits li{font-size:10px;line-height:16.3px;display:flex;align-items:center;gap:7px;color:#222}
.benefits li svg{flex:none}
.call-band{left:0;top:475px;width:530px;height:48px;background:linear-gradient(90deg,var(--gold-deep),var(--gold-light) 40%,var(--gold) 100%);z-index:3}
.call-band .circle{position:absolute;left:20px;top:8px;width:32px;height:32px;border-radius:50%;background:var(--navy);display:flex;align-items:center;justify-content:center}
.call-band p{position:absolute;left:67px;top:7px;font-size:13px;line-height:17px;color:var(--navy-deep)}
.call-band p i{font-weight:700;font-size:14px}
.brand-plate{left:-40px;top:545px;width:260px;height:180px;border-radius:50% 50% 0 0;background:#fff}
.brand-plate-name{left:10px;top:585px;width:190px;text-align:center;font-family:"Roboto",sans-serif;font-weight:700;font-size:19px;line-height:22px;color:var(--royal)}
.front-contact{left:220px;top:533px;width:310px;color:#fff}
.phone-row{display:flex;align-items:center;gap:8px;padding-left:18px}
.phone-row .ic{width:30px;height:30px;border-radius:50%;background:var(--gold);display:flex;align-items:center;justify-content:center}
.phone-row span{font-family:"Roboto Condensed",sans-serif;font-weight:700;font-size:30px}
.web-row{display:flex;align-items:center;gap:10px;padding-left:22px;margin-top:7px;font-family:"Roboto Condensed",sans-serif;font-weight:500;font-size:19px}
.nmls{display:flex;align-items:center;justify-content:center;gap:10px;font-size:12.5px;font-weight:500}
.nmls:before,.nmls:after{content:"";width:55px;height:1.5px;background:var(--gold)}
.front-contact .nmls{margin-top:9px}
/* back */
.back-header{left:0;top:0;width:530px;height:98px;background:linear-gradient(180deg,var(--navy-deep),var(--royal))}
.back-header svg.house{position:absolute;left:16px;top:16px}
.back-title{left:96px;top:14px;font-family:"Oswald",sans-serif;font-weight:700;font-size:40px;line-height:36px;color:#fff;letter-spacing:.5px;white-space:nowrap}
.back-title span{color:var(--gold);display:block}
.header-swoosh{left:0;top:84px}
.photo-house-back{left:283px;top:106px;width:247px;height:208px;background:linear-gradient(90deg,rgba(255,255,255,1) 0%,rgba(255,255,255,0) 30%),linear-gradient(180deg,#cfe0f2 0%,#e8e4dc 55%,#5f8f3f 100%)}
.notices{left:21px;top:113px;z-index:2}
.notices h3{font-size:14px;color:var(--royal);font-weight:700}
.notices ul{list-style:none;margin-top:8px}
.notices li{font-size:12px;line-height:22.7px;color:#1d2230;display:flex;align-items:center;gap:10px}
.notices li:before{content:"";width:5px;height:5px;border-radius:50%;background:var(--navy)}
.qualify{left:21px;top:259px;width:350px;font-size:11.5px;line-height:16px;font-style:italic;color:#222;z-index:2}
.qualify b{color:var(--royal)}
.divider{left:20px;top:305px;width:490px;height:1.5px;background:var(--gold)}
.diamond{left:251px;top:302px;width:7px;height:7px;background:var(--gold-deep);transform:rotate(45deg)}
.programs-intro{left:0;top:316px;width:530px;text-align:center;font-size:13.5px;line-height:17px;font-weight:700;color:var(--royal)}
.programs{left:0;top:354px;width:530px;display:flex}
.program{width:132.5px;text-align:center;position:relative}
.program+.program:before{content:"";position:absolute;left:0;top:8px;width:1.5px;height:95px;background:var(--gold)}
.program .badge{width:58px;height:58px;margin:0 auto;border-radius:50%;background:var(--royal);border:3px solid var(--gold);display:flex;align-items:center;justify-content:center}
.program p{margin-top:8px;font-size:12.5px;line-height:14.5px;font-weight:500;color:#111}
.offer-band{left:0;top:476px;width:530px;height:32px;background:linear-gradient(90deg,var(--gold-deep),var(--gold-light) 50%,var(--gold-deep))}
.offer-band p{text-align:center;font-family:"Roboto Condensed",sans-serif;font-weight:700;font-size:20px;line-height:32px;color:var(--navy-deep);letter-spacing:.3px}
.back-footer{left:0;top:508px;width:530px;height:138px;background:linear-gradient(135deg,var(--navy-deep),var(--royal))}
.portrait{left:22px;top:514px;width:124px;height:124px;border-radius:50%;border:4px solid var(--gold);background:linear-gradient(180deg,#4a5e92,#1b1f2e)}
.contact{left:166px;top:512px;color:#fff}
.contact .script{font-family:"Great Vibes",cursive;font-size:26px;line-height:24px}
.contact .name{font-family:"Oswald",sans-serif;font-weight:700;font-size:38px;line-height:38px;color:var(--gold);letter-spacing:.5px;white-space:nowrap}
.contact .line{font-size:16px;line-height:22px;font-weight:500}
.contact .line b{font-family:"Roboto Condensed",sans-serif;font-size:22px;color:var(--gold)}
.contact .email{font-size:17px;line-height:22px;font-weight:500}
.contact .nmls{margin-top:4px;font-size:11.5px}
.contact .nmls:before,.contact .nmls:after{width:75px}
</style>
</head>
<body>

<header class="brand-band">
  <span class="dot"></span>
  <span class="name">Bluegate Lending Partners</span>
</header>

<section class="card card-front">
  <div class="ph photo-collage" role="img" aria-label="Photo collage of a stressed couple and a worried man over paperwork, with a city skyline at sunset"></div>
  <div class="ph head-fade"></div>
  <div class="ph photo-advisor" role="img" aria-label="Portrait photo of the loan officer in a black hat and jacket"></div>

  <h1 class="abs headline">
    <span class="small">Is a</span>
    <span class="big">PROPERTY LIEN</span>
    <span class="mid l3">Putting Your Home</span>
    <span class="mid l4">at <span class="gold">Risk?</span></span>
  </h1>

  <div class="abs lien-band"></div>
  <p class="abs lien-text">HOA LIENS <b>•</b> TAX LIENS <b>•</b> MUNICIPAL CHARGES<br><b>•</b> OTHER PROPERTY-RELATED LIENS</p>

  <div class="abs options"><p>You may have options to resolve outstanding<br>liens and <em>protect your home.</em></p></div>

  <div class="abs benefits-bg"></div>
  <div class="ph photo-house-front" role="img" aria-label="Photo of a stone and shingle family home with landscaped lawn"></div>
  <div class="abs benefits">
    <h3>A Refinance or Home Equity Line of Credit (HELOC) may help you:</h3>
    <ul>
      <li><svg width="12" height="12" viewBox="0 0 12 12"><circle cx="6" cy="6" r="6" fill="#e0a624"/><path d="M3 6.2l2 2 4-4.2" stroke="#fff" stroke-width="1.6" fill="none"/></svg>Pay off qualifying liens</li>
      <li><svg width="12" height="12" viewBox="0 0 12 12"><circle cx="6" cy="6" r="6" fill="#e0a624"/><path d="M3 6.2l2 2 4-4.2" stroke="#fff" stroke-width="1.6" fill="none"/></svg>Consolidate debt into one manageable payment</li>
      <li><svg width="12" height="12" viewBox="0 0 12 12"><circle cx="6" cy="6" r="6" fill="#e0a624"/><path d="M3 6.2l2 2 4-4.2" stroke="#fff" stroke-width="1.6" fill="none"/></svg>Access your home’s equity</li>
      <li><svg width="12" height="12" viewBox="0 0 12 12"><circle cx="6" cy="6" r="6" fill="#e0a624"/><path d="M3 6.2l2 2 4-4.2" stroke="#fff" stroke-width="1.6" fill="none"/></svg>Improve your financial flexibility</li>
      <li><svg width="12" height="12" viewBox="0 0 12 12"><circle cx="6" cy="6" r="6" fill="#e0a624"/><path d="M3 6.2l2 2 4-4.2" stroke="#fff" stroke-width="1.6" fill="none"/></svg>Avoid additional penalties, fees, or collection actions</li>
    </ul>
  </div>

  <div class="abs call-band">
    <div class="circle"><svg width="16" height="16" viewBox="0 0 24 24"><path fill="#fff" d="M6.6 10.8a15 15 0 006.6 6.6l2.2-2.2c.3-.3.7-.4 1-.2 1.1.4 2.3.6 3.6.6.6 0 1 .4 1 1V20c0 .6-.4 1-1 1A17 17 0 013 4c0-.6.4-1 1-1h3.5c.6 0 1 .4 1 1 0 1.3.2 2.5.6 3.6.1.3 0 .7-.2 1z"/></svg></div>
    <p>Don’t wait until the situation becomes more difficult.<br><i>Call today for a confidential review of your options.</i></p>
  </div>

  <div class="abs brand-plate"></div>
  <p class="abs brand-plate-name">Bluegate Lending<br>Partners, Inc.</p>

  <div class="abs front-contact">
    <div class="phone-row">
      <span class="ic"><svg width="16" height="16" viewBox="0 0 24 24"><path fill="#fff" d="M6.6 10.8a15 15 0 006.6 6.6l2.2-2.2c.3-.3.7-.4 1-.2 1.1.4 2.3.6 3.6.6.6 0 1 .4 1 1V20c0 .6-.4 1-1 1A17 17 0 013 4c0-.6.4-1 1-1h3.5c.6 0 1 .4 1 1 0 1.3.2 2.5.6 3.6.1.3 0 .7-.2 1z"/></svg></span>
      <span>(800) 647-2915 x 42</span>
    </div>
    <div class="web-row">
      <svg width="22" height="22" viewBox="0 0 24 24" fill="none" stroke="#fff" stroke-width="1.6"><circle cx="12" cy="12" r="10"/><ellipse cx="12" cy="12" rx="4.5" ry="10"/><path d="M2 12h20M4 7h16M4 17h16"/></svg>
      <span>www.bluegatelendco.com</span>
    </div>
    <p class="nmls">NMLS #381640</p>
  </div>
</section>

<section class="card card-back">
  <div class="abs back-header">
    <svg class="house" width="66" height="66" viewBox="0 0 66 66" fill="none" stroke="#f2c230" stroke-width="6" stroke-linejoin="round"><path d="M4 32L33 6l29 26"/><path d="M13 26v28h40V26"/><path d="M27 54V40h12v14"/><path d="M2 62h62" stroke-width="4"/></svg>
  </div>
  <h2 class="abs back-title">YOUR HOME EQUITY<span>COULD BE THE SOLUTION</span></h2>
  <svg class="abs header-swoosh" width="530" height="22" viewBox="0 0 530 22"><path d="M0 14 Q265 -4 530 8" stroke="#f2c230" stroke-width="3" fill="none"/></svg>

  <div class="ph photo-house-back" role="img" aria-label="Photo of a white two-story house with porch, walkway and green lawn"></div>

  <div class="abs notices">
    <h3>If you have received notices regarding:</h3>
    <ul>
      <li>Delinquent Property Taxes</li>
      <li>HOA or Condo Association Assessments</li>
      <li>Municipal Utility Liens</li>
      <li>Special Assessments</li>
      <li>Other Property-Related Obligations</li>
    </ul>
  </div>
  <p class="abs qualify">You may qualify for financing options designed to help satisfy<br>those obligations and <b>bring your property current.</b></p>

  <div class="abs divider"></div>
  <div class="abs diamond"></div>

  <p class="abs programs-intro">Our experienced mortgage professionals can<br>review your situation and discuss available programs, including:</p>

  <div class="abs programs">
    <div class="program">
      <div class="badge"><svg width="32" height="32" viewBox="0 0 32 32" fill="none" stroke="#fff" stroke-width="2.4"><path d="M3 15L16 4l13 11"/><path d="M7 12v15h18V12"/><circle cx="16" cy="19" r="5"/><path d="M16 16v6" stroke-width="1.6"/></svg></div>
      <p>Cash-Out<br>Refinancing</p>
    </div>
    <div class="program">
      <div class="badge"><svg width="32" height="32" viewBox="0 0 32 32" fill="none" stroke="#fff" stroke-width="2.4"><rect x="4" y="8" width="24" height="16" rx="2"/><path d="M4 13h24"/><path d="M8 19h6"/></svg></div>
      <p>Home Equity<br>Lines of Credit<br>(HELOCs)</p>
    </div>
    <div class="program">
      <div class="badge"><svg width="32" height="32" viewBox="0 0 32 32" fill="none" stroke="#fff" stroke-width="2.4"><path d="M3 15L15 4l12 11"/><path d="M7 12v15h10"/><circle cx="23" cy="22" r="6" fill="#fff"/><path d="M23 18.5v7" stroke="#1d47a8" stroke-width="1.8"/></svg></div>
      <p>Home Equity<br>Loans</p>
    </div>
    <div class="program">
      <div class="badge"><svg width="34" height="28" viewBox="0 0 34 28" fill="#fff"><circle cx="17" cy="8" r="5"/><path d="M8 24c0-6 4-9 9-9s9 3 9 9z"/><circle cx="7" cy="10" r="3.5"/><path d="M0 23c0-4 3-6 7-6 1 0 2 .2 2.5.5-1.3 1.5-2 3.5-2 5.5z"/><circle cx="27" cy="10" r="3.5"/><path d="M34 23c0-4-3-6-7-6-1 0-2 .2-2.5.5 1.3 1.5 2 3.5 2 5.5z"/></svg></div>
      <p>Debt<br>Consolidation<br>Solutions</p>
    </div>
  </div>

  <div class="abs offer-band"><p>FREE CONSULTATION &nbsp;•&nbsp; NO OBLIGATION</p></div>

  <div class="abs back-footer"></div>
  <div class="ph portrait" role="img" aria-label="Circular portrait photo of Marcus Delaney"></div>
  <div class="abs contact">
    <p class="script">Contact</p>
    <p class="name">MARCUS DELANEY</p>
    <p class="line">today at <b>(800) 647-2915 x42</b></p>
    <p class="email">or mdelaney@bluegatelendco.com</p>
    <p class="nmls">NMLS #57308</p>
  </div>
</section>

</body>
</html>
```